Roll-up-Banner für Schule gesucht
Zielgruppe
Unsere Schule wünscht einen Rollup (880mm Breite x 2200mm Höhe) für die jährliche Lesenacht für Kinder im Alter von 6-12 Jahren. Diese wären die Produktdaten: https://blaetter.vimtral-laden.de/ro-04-85-roll-up-display-basic-85-produktblatt-productsheet.pdf
Der Rollup sollte für Kinder kreiert werden aber nicht zu kindlich sein.
Aufgabenstellung
Das Logo der Schule müsste ersichtlich sein ansonsten ist Kreativität gefragt ;-)

```html
<!DOCTYPE html>
<html lang="de">
<head>
<meta charset="utf-8">
<title>Lesenacht für Kinder – Roll-up</title>
<link rel="stylesheet" href="https://fonts.googleapis.com/css2?family=Archivo:wght@700;800&display=swap">
<style>
  :root {
    --page: #ffffff;
    --frame: #3a3a3a;
    --sky-top: #66758c;
    --sky-mid: #c6c3c8;
    --haze: #d8b3a0;
    --dusk: #b08476;
    --ground: #8a6c55;
    --cape: #b8323a;
    --cape-soft: rgba(184, 50, 58, 0);
    --stone: #a08a6e;
    --headline: #ffffff;
    --brand-text: #1f1f1f;
    --brand-green: #1f9a4a;
  }
  html, body {
    margin: 0;
    padding: 0;
    width: 1200px;
    height: 1200px;
    overflow: hidden;
    background: var(--page);
  }
  .canvas {
    position: relative;
    width: 1200px;
    height: 1200px;
  }
  .rollup {
    position: absolute;
    left: 408px;
    top: 52px;
    width: 422px;
    height: 1096px;
    box-sizing: border-box;
    border: 1px solid var(--frame);
    background: var(--page);
    overflow: hidden;
  }
  .rollup__visual {
    position: absolute;
    left: 0;
    top: 0;
    width: 100%;
    height: 826px;
    background:
      radial-gradient(ellipse 260px 300px at 110px 470px, var(--cape) 0%, var(--cape-soft) 100%),
      linear-gradient(180deg,
        var(--sky-top) 0%,
        var(--sky-mid) 26%,
        var(--haze) 56%,
        var(--dusk) 78%,
        var(--stone) 88%,
        var(--ground) 100%);
  }
  .rollup__headline {
    position: absolute;
    left: 0;
    top: 0;
    width: 100%;
    height: 826px;
  }
  .rollup__headline text {
    font-family: "Archivo", Arial, sans-serif;
    font-weight: 800;
    font-size: 78px;
    fill: var(--headline);
  }
  .brand {
    position: absolute;
    left: 0;
    top: 826px;
    width: 100%;
    height: 140px;
    display: flex;
    align-items: center;
    justify-content: center;
    gap: 12px;
  }
  .brand__mark {
    width: 22px;
    height: 22px;
    border-radius: 50%;
    background: var(--brand-green);
  }
  .brand__name {
    font-family: "Archivo", Arial, sans-serif;
    font-weight: 800;
    font-size: 21px;
    letter-spacing: 5px;
    color: var(--brand-text);
  }
</style>
</head>
<body>
<div class="canvas">
  <div class="rollup">
    <div class="rollup__visual" role="img" aria-label="Foto: Mädchen mit rotem Superhelden-Umhang steht von hinten gesehen auf einem Steinsockel und blickt in den Abendhimmel über der Stadt"></div>
    <svg class="rollup__headline" width="422" height="826" viewBox="0 0 422 826">
      <text x="0" y="0" transform="translate(398 806) rotate(-90)" textLength="756" lengthAdjust="spacingAndGlyphs">Lesenacht für Kinder</text>
    </svg>
    <div class="brand">
      <span class="brand__mark"></span>
      <span class="brand__name">SCHULE ELMSTAL</span>
    </div>
  </div>
</div>
</body>
</html>
```